Pebblo Bites - Product Packaging (Snack wrapper)

Pebblo Bites is looking for our next package design! Our snack products are all-natural, gluten-free, vegan, and paleo. Our mission is to bring clean, wholesome snacks back into the market. The package design is for our individual wrappers that hold two of our snack bites.

The background will be matte white with a transparent window integrated so that customers can see the bites inside.

The final design will be clean and modern, using white as the background, black for text, and our logos yellow. We have multiple different flavors, so each flavor will have its own unique color accents that must be editable in the final file. The accent colors should be bold and take up an equal amount of space as the white does.

The packaging will stand out on a busy shelf and entice customers as an easy on-the-go, wholesome snack. The back of the package must have a space for a nutrition box and ingredients list. Our logo is attached. The logo graphic can be separated (it doesnt have to stay in the same layout you see). We have attached an example of our old product label, too.

The package dimensions are 4inches wide x 5 inches long with a 1/2inch of the length at the top and 1/2inch of the length at the bottom being blank for sealing. Thank you!

Target Market(s)

Cafe goers, health-conscience, kids, active.

Font styles to use
Sans Serif

Colors
fbed22
ffffff
000000

Requirements
Must have
• Must show that our product is gluten-free, vegan, and paleo. Must have editable flavor name, and flavor accent colors for our multiple different flavors. Must use our logo and company yellow.

```html
<!DOCTYPE html>
<html lang="en">
<head>
<meta charset="utf-8">
<title>Pebblo Bites – Snack Wrappers</title>
<link rel="stylesheet" href="https://fonts.googleapis.com/css2?family=Dancing+Script:wght@500;600&family=Comfortaa:wght@400&display=swap">
<style>
  :root {
    --page-bg: #f4f4f6;
    --wrapper-white: #fbfbfb;
    --wrapper-edge: #e4e4e8;
    --seal-tint: #ededf0;
    --brand-yellow: #e3c64a;
    --choc-accent: #b3604a;
    --choc-ink: #6a2016;
    --lemon-accent: #c3d52c;
    --lemon-ink: #7d901c;
    --photo-choc: #c69a66;
    --photo-lemon: #d9b98a;
    --band-text: #ffffff;
  }
  * { margin: 0; padding: 0; box-sizing: border-box; }
  html, body { width: 1200px; height: 1000px; overflow: hidden; background: var(--page-bg); }
  .stage { position: relative; width: 1200px; height: 1000px; }

  .wrapper {
    position: absolute;
    background: var(--wrapper-white);
    border: 1px solid var(--wrapper-edge);
    box-shadow: 0 6px 18px rgba(0,0,0,0.08);
    overflow: hidden;
  }
  .wrapper::before, .wrapper::after {
    content: ""; position: absolute; left: 0; right: 0; height: 34px; background: var(--seal-tint);
  }
  .wrapper::before { top: 0; }
  .wrapper::after { bottom: 0; }
  .wrapper--lemon { left: 570px; top: 185px; width: 540px; height: 550px; }
  .wrapper--choc { left: 55px; top: 215px; width: 580px; height: 590px; }

  .brand { position: absolute; display: flex; align-items: center; gap: 14px; }
  .brand__dot { border-radius: 50%; background: var(--brand-yellow); flex: none; }
  .brand__name {
    font-family: "Dancing Script", cursive; font-weight: 600;
    color: var(--brand-yellow); line-height: 1; white-space: nowrap;
  }

  .accent-line { position: absolute; }
  .accent-band { position: absolute; display: flex; align-items: center; }
  .accent-band__text {
    font-family: "Comfortaa", sans-serif; color: var(--band-text); letter-spacing: 1px; white-space: nowrap;
  }
  .flavor { position: absolute; text-align: center; font-family: "Dancing Script", cursive; font-weight: 600; line-height: 1; }
  .flavor__name { display: block; }
  .flavor__sub { display: block; }

  .product-window { position: absolute; border-radius: 50%; }

  /* Chocolate wrapper */
  .wrapper--choc .brand { left: 42px; top: 132px; }
  .wrapper--choc .brand__dot { width: 52px; height: 52px; }
  .wrapper--choc .brand__name { font-size: 62px; }
  .wrapper--choc .accent-line--top { left: 13px; top: 221px; width: 420px; height: 8px; background: var(--choc-accent); }
  .wrapper--choc .accent-line--bottom { left: 13px; top: 333px; width: 420px; height: 5px; background: var(--choc-accent); }
  .wrapper--choc .accent-band { left: 13px; top: 345px; width: 420px; height: 65px; background: var(--choc-accent); padding-left: 25px; }
  .wrapper--choc .accent-band__text { font-size: 19px; }
  .wrapper--choc .flavor { left: 40px; top: 234px; width: 300px; color: var(--choc-ink); }
  .wrapper--choc .flavor__name { font-size: 48px; }
  .wrapper--choc .flavor__sub { font-size: 36px; margin-top: 2px; }
  .wrapper--choc .product-window {
    left: 345px; top: 175px; width: 235px; height: 235px;
    background: radial-gradient(circle, var(--photo-choc) 55%, var(--choc-accent) 100%);
  }

  /* Lemon wrapper */
  .wrapper--lemon .brand { left: 48px; top: 100px; }
  .wrapper--lemon .brand__dot { width: 44px; height: 44px; }
  .wrapper--lemon .brand__name { font-size: 52px; }
  .wrapper--lemon .accent-line--top { left: 50px; top: 185px; width: 330px; height: 6px; background: var(--lemon-accent); }
  .wrapper--lemon .accent-line--bottom { left: 50px; top: 282px; width: 330px; height: 5px; background: var(--lemon-accent); }
  .wrapper--lemon .accent-band { left: 50px; top: 293px; width: 330px; height: 60px; background: var(--lemon-accent); padding-left: 8px; }
  .wrapper--lemon .accent-band__text { font-size: 17px; }
  .wrapper--lemon .flavor { left: 60px; top: 197px; width: 270px; color: var(--lemon-ink); }
  .wrapper--lemon .flavor__name { font-size: 42px; }
  .wrapper--lemon .flavor__sub { font-size: 32px; margin-top: 2px; }
  .wrapper--lemon .product-window {
    left: 335px; top: 138px; width: 210px; height: 210px;
    background: radial-gradient(circle, var(--photo-lemon) 55%, var(--lemon-accent) 100%);
  }
</style>
</head>
<body>
<main class="stage">

  <section class="wrapper wrapper--lemon" aria-label="Zesty Lemon wrapper">
    <div class="brand">
      <span class="brand__dot"></span>
      <span class="brand__name">Pebblo Bites</span>
    </div>
    <div class="accent-line accent-line--top"></div>
    <h2 class="flavor">
      <span class="flavor__name">Zesty Lemon</span>
      <span class="flavor__sub">Cookie Bites</span>
    </h2>
    <div class="accent-line accent-line--bottom"></div>
    <div class="accent-band"><span class="accent-band__text">Gluten Free - Vegan - Paleo</span></div>
    <div class="product-window" role="img" aria-label="Sun-shaped window showing lemon poppy seed cookie bites"></div>
  </section>

  <section class="wrapper wrapper--choc" aria-label="Chocolate Chip wrapper">
    <div class="brand">
      <span class="brand__dot"></span>
      <span class="brand__name">Pebblo Bites</span>
    </div>
    <div class="accent-line accent-line--top"></div>
    <h2 class="flavor">
      <span class="flavor__name">Chocolate Chip</span>
      <span class="flavor__sub">Cookie Bites</span>
    </h2>
    <div class="accent-line accent-line--bottom"></div>
    <div class="accent-band"><span class="accent-band__text">Gluten Free - Vegan - Paleo</span></div>
    <div class="product-window" role="img" aria-label="Sun-shaped window showing chocolate chip cookie bites"></div>
  </section>

</main>
</body>
</html>
```